Website redesign

Redesign the Website

http://www.lindmark-schoefer.de/

Task

- make 1 Layout for the Website
- Colors: white, yellow, brown
- Text: Take from Page - ore rather Use Latin - Lore Ipsum ...
- pimp design and overall look
- enhance overview for better orientation
- more freindly / sympatic overall look.
- Better integrate Mingleroo Button aso.
- send Layout as layered PSD

```html
<!DOCTYPE html>
<html lang="de">
<head>
<meta charset="utf-8">
<title>Lindmark Schöfer – Trauringe</title>
<link href="https://fonts.googleapis.com/css2?family=Great+Vibes&family=Open+Sans:wght@400;600;700&family=Playfair+Display:wght@400;700&display=swap" rel="stylesheet">
<style>
:root{
  --yellow:#f2c230;
  --brown:#6b3a12;
  --brown-soft:#8a5a2b;
  --red-brown:#a03a16;
  --dark:#151515;
  --footer:#1d1f22;
  --text:#444;
  --muted:#9a9a9a;
  --white:#fff;
}
*{margin:0;padding:0;box-sizing:border-box}
html,body{width:783px;height:1200px;overflow:hidden;background:var(--white)}
body{position:relative;font-family:'Open Sans',Arial,sans-serif;color:var(--text)}
.abs{position:absolute}

/* header */
.brand{left:52px;top:12px;height:58px;display:flex;align-items:center;gap:8px}
.brand-mark{width:14px;height:14px;border-radius:50%;background:var(--yellow)}
.brand-name{font-family:'Playfair Display',serif;font-weight:700;font-size:19px;line-height:21px;color:var(--brown)}
.social{display:flex;gap:6px}
.social span{width:15px;height:15px;border-radius:50%;display:block}
.header-social{left:456px;top:33px}
.s1{background:#3b5998}.s2{background:#2aa6de}.s3{background:#d4463a}.s4{background:#a14aa6}
.search{left:580px;top:32px;width:110px;height:18px;border:1px solid #ccc;font-size:8px;color:var(--muted);padding:3px 6px}
.search svg{position:absolute;right:4px;top:3px}

/* nav */
.nav{left:52px;top:88px;width:680px;height:26px;background:var(--yellow);display:flex;justify-content:space-between;padding:0 30px 0 0}
.nav a{font-size:9px;color:var(--brown);text-decoration:none;line-height:26px;padding:0 14px}
.nav a.active{background:var(--brown);color:var(--white);padding:0 20px}

/* hero */
.hero{left:52px;top:117px;width:680px;height:285px;background:linear-gradient(120deg,#f4f4f4 0%,#dcdcdc 35%,#c9b28a 55%,#e9e9e9 70%,#d8b45a 90%,#f2f2f2 100%)}
.hero-title{left:52px;top:124px;width:680px;text-align:center;font-family:'Great Vibes',cursive;font-size:30px;color:var(--brown-soft)}
.dots{left:365px;top:388px;display:flex;gap:5px}
.dots i{width:6px;height:6px;border-radius:50%;background:#bbb;display:block}
.dots i:first-child{background:var(--brown)}

/* welcome */
.welcome{left:52px;top:408px;width:680px;text-align:center}
.welcome-small{font-family:'Playfair Display',serif;font-size:14px;color:var(--brown);font-weight:700}
.welcome-big{font-family:'Playfair Display',serif;font-size:15px;color:var(--red-brown);font-weight:700;letter-spacing:.5px;margin-top:-2px}
.divider{display:flex;align-items:center;justify-content:center;gap:6px;margin-top:6px}
.divider .line{width:24px;height:1px;background:#ccc}
.divider .ornament{width:18px;height:12px;border-radius:3px;background:linear-gradient(180deg,#c8c8c8,#8e8e8e)}
.welcome-text{width:510px;margin:10px auto 0;font-size:7.5px;line-height:12px;color:#666}
.btn-more{left:352px;top:562px;width:76px;height:22px;background:var(--brown);color:var(--white);font-size:7.5px;font-weight:600;line-height:22px;text-align:center}

/* promos */
.promo{top:690px;width:337px;height:139px;background:var(--dark)}
.promo-left{left:52px}
.promo-right{left:393px}
.promo h3{position:absolute;left:18px;top:12px;font-family:'Playfair Display',serif;font-weight:400;font-size:14px;color:var(--white)}
.promo p{position:absolute;left:18px;top:36px;width:120px;font-size:7.5px;line-height:11px;color:#ddd}
.promo .more{position:absolute;left:18px;top:110px;width:40px;height:14px;background:var(--yellow);color:var(--brown);font-size:6px;font-weight:700;text-align:center;line-height:14px}
.promo .photo{position:absolute;right:10px;top:28px;width:170px;height:108px}
.promo-left .photo{background:radial-gradient(ellipse at center,#d8d8d8 0%,#8f8f8f 40%,#1a1a1a 72%)}
.promo-right .photo{background:radial-gradient(ellipse at center,#f0cf6a 0%,#b08a2a 40%,#161616 72%)}

/* strip */
.strip{left:0;top:831px;width:783px;height:170px;display:flex}
.strip div{flex:1}
.t1{background:linear-gradient(135deg,#f2f2f2,#b8b8b8)}
.t2{background:linear-gradient(135deg,#6b4020,#a0703c);position:relative}
.t3{background:linear-gradient(135deg,#9fc7c4,#e6eeee)}
.t4{background:linear-gradient(135deg,#eeeeee,#c7a27a)}
.t5{background:linear-gradient(135deg,#e8e8e8,#9a9a9a)}
.zoom{position:absolute;left:50%;top:50%;transform:translate(-50%,-50%)}

/* footer */
.footer{left:0;top:1001px;width:783px;height:199px;background:var(--footer)}
.fcol{top:1028px}
.fcol h4{font-size:9px;font-weight:600;color:var(--white);letter-spacing:.4px;margin-bottom:9px}
.fcol ul{list-style:none}
.fcol li{font-size:6.5px;color:#bbb;line-height:15px;padding-left:10px;position:relative}
.fcol li::before{content:"";position:absolute;left:0;top:6px;width:3px;height:3px;border-radius:50%;background:var(--yellow)}
.col-main{left:72px}
.col-links{left:220px}
.col-news{left:380px;width:160px}
.col-news p{font-size:6.5px;color:#bbb;margin-bottom:8px}
.field{width:100px;height:16px;background:#3a3c40;color:#aaa;font-size:6.5px;line-height:16px;padding-left:6px;margin-bottom:6px}
.send{width:40px;height:16px;background:var(--yellow);color:var(--brown);font-size:7px;font-weight:700;text-align:center;line-height:16px}
.footer-brand{left:570px;top:1050px;display:flex;align-items:center;gap:6px}
.footer-brand .brand-name{color:var(--white);font-size:17px;line-height:19px}
.footer-social{left:72px;top:1172px}
.footer-social span{width:10px;height:10px}
.copyright{left:520px;top:1172px;width:230px;text-align:right;font-size:6px;color:var(--muted)}
</style>
</head>
<body>

<header>
  <div class="abs brand">
    <span class="brand-mark"></span>
    <span class="brand-name">Lindmark<br>Schöfer.de</span>
  </div>
  <div class="abs social header-social" aria-label="Soziale Netzwerke">
    <span class="s1" title="Mingleroo"></span><span class="s2"></span><span class="s3"></span><span class="s4"></span>
  </div>
  <div class="abs search">Search here...
    <svg width="10" height="10" viewBox="0 0 10 10"><circle cx="4" cy="4" r="3" fill="none" stroke="#999" stroke-width="1.2"/><line x1="6.3" y1="6.3" x2="9" y2="9" stroke="#999" stroke-width="1.2"/></svg>
  </div>
  <nav class="abs nav">
    <a class="active">Trauringe</a><a>Solitärringe</a><a>Partnerringe</a><a>Brautschmuck</a><a>Informationen</a><a>Kontakt</a>
  </nav>
</header>

<section>
  <div class="abs hero" role="img" aria-label="Trauringpaare in Silber, Roségold und Gold auf hellem Grund"></div>
  <div class="abs hero-title">Die schönsten Trauringe...</div>
  <div class="abs dots"><i></i><i></i><i></i><i></i></div>
</section>

<section class="abs welcome">
  <div class="welcome-small">welcome</div>
  <div class="welcome-big">TO OUR STORE!</div>
  <div class="divider">
    <span class="line"></span>
    <span class="ornament" role="img" aria-label="Kleines Ringpaar als Zierelement"></span>
    <span class="line"></span>
  </div>
  <p class="welcome-text">Lorem Ipsum is simply dummy text of the printing and typesetting industry. Lorem Ipsum has been the industry's standard dummy text ever since the 1500s. Lorem Ipsum is simply dummy text of the printing and typesetting industry. Lorem Ipsum has been the industry's standard dummy text ever since the 1500s. Lorem Ipsum is simply dummy text of the printing and typesetting industry. Lorem Ipsum has been the industry's standard.</p>
</section>
<div class="abs btn-more">LEARN MORE</div>

<section>
  <div class="abs promo promo-left">
    <h3>Die schönsten Trauringe...</h3>
    <p>Lorem Ipsum is simply dummy text of the printing and typesetting industry.</p>
    <div class="more">MORE</div>
    <div class="photo" role="img" aria-label="Zwei silberne Trauringe mit Steinbesatz"></div>
  </div>
  <div class="abs promo promo-right">
    <h3>Die schönsten Trauringe...</h3>
    <p>Lorem Ipsum is simply dummy text of the printing and typesetting industry.</p>
    <div class="more">MORE</div>
    <div class="photo" role="img" aria-label="Zwei goldene Trauringe"></div>
  </div>
</section>

<section class="abs strip">
  <div class="t1" role="img" aria-label="Silberne Ringe"></div>
  <div class="t2" role="img" aria-label="Ringe auf braunem Grund">
    <svg class="zoom" width="18" height="18" viewBox="0 0 18 18"><rect width="18" height="18" fill="rgba(0,0,0,.4)"/><circle cx="8" cy="8" r="4" fill="none" stroke="#fff" stroke-width="1.3"/><line x1="11" y1="11" x2="14" y2="14" stroke="#fff" stroke-width="1.3"/></svg>
  </div>
  <div class="t3" role="img" aria-label="Ringe mit türkisem Akzent"></div>
  <div class="t4" role="img" aria-label="Ringe in Silber und Rosé"></div>
  <div class="t5" role="img" aria-label="Silberne Ringe auf Weiß"></div>
</section>

<footer>
  <div class="abs footer"></div>
  <div class="abs fcol col-main">
    <h4>MAIN MENU</h4>
    <ul><li>Trauringe</li><li>Solitärringe</li><li>Partnerringe</li><li>Brautschmuck</li><li>Informationen</li><li>Kontakt</li></ul>
  </div>
  <div class="abs fcol col-links">
    <h4>QUICK LINK</h4>
    <ul><li>Customer Policy</li><li>Our Policy</li><li>Terms and conditions of use</li><li>Service payment</li><li>Sitemap</li></ul>
  </div>
  <div class="abs fcol col-news">
    <h4>NEWSLATTER SIGN UP</h4>
    <p>Lorem ipsum dolor sit amet</p>
    <div class="field">Your Name</div>
    <div class="field">Email ID</div>
    <div class="send">Send</div>
  </div>
  <div class="abs footer-brand">
    <span class="brand-mark"></span>
    <span class="brand-name">Lindmark<br>Schöfer.de</span>
  </div>
  <div class="abs social footer-social">
    <span class="s1"></span><span class="s2"></span><span class="s3"></span><span class="s4"></span>
  </div>
  <div class="abs copyright">©2014 Lindmark-Schöfer All Rights Reserved</div>
</footer>

</body>
</html>
```